Exciting Wordpress Project: New Consulting Firm

A wordpress design is needed for my new consulting company, Verbrook Partners.

The site should have a modern feel to it and use the colour scheme from the attached 3 vector files.

I only know a little about Wordpress but the site should be mobile friendly.

The following menu options should be created:
1. Home
2. Verbrook service lines (with sub-menus)
3. Our people
4. Verbrook case studies
5. The Verbrook story
6. Contact Verbrook
Updates

Reason: Allow just one or two more designs to come in before deciding.

Target Market(s)

Government departments and medium private sector organisations

Industry/Entity Type

It Company

Requirements
Must have
• 1. Inclue Verbrook logo at top of each page
2. Slider on the home page
3. Global navigation
4. Drop down navigation
5. Social media links
6. Search and contact details at the top of the home page
7. Home page to fit on one screen
8. Terms & Conditions, Privacy Policy at the bottom of the home page
9. Newsletter (i.e. postwren) subscription on home page
Nice to have
• 1. Background watermark from the Verbrook logo
2. A layout similar to the photo attached - however open to different ideas

```html
<!DOCTYPE html>
<html lang="en">
<head>
<meta charset="utf-8">
<title>Verbrook Partners — Home</title>
<link rel="stylesheet" href="https://fonts.googleapis.com/css2?family=Bebas+Neue&family=Oswald:wght@400&family=Arimo:wght@400;700&family=Open+Sans:wght@400;600&display=swap">
<style>
:root{
  --brand:#2a4a9c;
  --brand-dark:#1f3a84;
  --ink:#555555;
  --heading:#5a5a5a;
  --rule:#e2e2e2;
  --footer:#58585a;
  --footer-text:#c9c9c9;
  --photo-mid:#8e8e8e;
}
*{box-sizing:border-box;margin:0;padding:0}
html,body{width:1053px;height:1200px;overflow:hidden;background:#fff}
body{position:relative;font-family:"Arimo",Arial,sans-serif;color:var(--ink);font-size:11px}
a{color:inherit}
.abs{position:absolute}

/* top bar */
.top-mail{left:92px;top:21px;display:flex;align-items:center;gap:8px;color:var(--brand-dark);font-size:11px;letter-spacing:.3px}
.search{left:551px;top:14px;width:312px;height:27px;border:1px solid #d6d6d6;background:#fff;display:flex;align-items:center}
.search span{flex:1;padding-left:14px;font-size:10px;color:#777}
.search i{width:38px;height:100%;border-left:1px solid #e3e3e3;display:flex;align-items:center;justify-content:center}
.social{left:881px;top:14px;display:flex;gap:3px}
.social b{width:26px;height:26px;border-radius:50%;background:var(--brand-dark);display:block}

/* header */
.header{left:0;top:61px;width:1053px;height:81px;background:linear-gradient(#f1f1f1,#fafafa 60%,#ececec);border-top:1px solid #e6e6e6}
.logo{left:92px;top:83px;color:#5d5d5d;font-family:"Open Sans",sans-serif;font-weight:400;line-height:1}
.logo .name{font-size:30px;letter-spacing:1px;display:block}
.logo .sub{font-size:8px;letter-spacing:9.5px;display:block;margin-top:2px}
.nav{left:296px;top:97px;display:flex;white-space:nowrap;font-family:"Open Sans",sans-serif;font-size:11px;color:#666;letter-spacing:.2px}
.nav a{text-decoration:none;padding:0 8px;border-left:1px dotted #bbb;line-height:15px}
.nav a:first-child{border-left:0;padding-left:0;color:var(--brand)}
.nav-marker{left:290px;top:61px;width:45px;height:6px;background:var(--brand)}

/* slider */
.slider{left:0;top:142px;width:1053px;height:304px;background:linear-gradient(180deg,#6d6d6d,#9a9a9a 40%,#5a5a5a)}
.arrow{top:243px;width:68px;height:53px;background:rgba(200,200,200,.5);display:flex;align-items:center;justify-content:center}

/* welcome */
.welcome{left:88px;top:482px;width:879px;height:102px;border:1px solid #e0e0e0;border-left:4px solid var(--brand);background:linear-gradient(#fff 40%,#ececec)}
.welcome h1{position:absolute;left:24px;top:16px;font-family:"Bebas Neue",sans-serif;font-weight:400;font-size:58px;color:var(--brand);letter-spacing:.5px}
.welcome .sep{position:absolute;left:211px;top:16px;height:54px;border-left:1px dotted #bbb}
.welcome p{position:absolute;left:231px;top:32px;width:485px;font-size:11px;line-height:14px;color:#666}
.btn{position:absolute;left:742px;top:29px;width:115px;height:33px;border-radius:4px;background:linear-gradient(#6e6e6e,#3f3f3f);color:#fff;font-family:"Oswald",sans-serif;font-size:16px;display:flex;align-items:center;justify-content:center;box-shadow:0 1px 2px rgba(0,0,0,.4)}

.hr{left:88px;width:880px;border-top:1px solid var(--rule)}
.vr{border-left:1px dotted #ccc}

h2{font-family:"Bebas Neue",sans-serif;font-weight:400;font-size:31px;line-height:1;color:var(--heading)}
h2.blue{color:var(--brand)}

/* about cards */
.card{top:686px;width:180px}
.card .thumb{width:180px;height:120px;border:2px solid #c8c8c8;position:relative;background:linear-gradient(#d9d9d9,var(--photo-mid))}
.card .label{position:absolute;left:0;bottom:0;width:100%;height:19px;background:var(--brand);color:#fff;font-family:"Open Sans",sans-serif;font-weight:600;font-size:12px;padding-left:9px;line-height:19px}
.card p{margin-top:16px;font-size:11px;line-height:14px;color:#666}
.more{font-family:"Open Sans",sans-serif;font-size:10px;color:#666;text-decoration:underline}

/* news */
.news{left:744px;width:220px;display:flex;gap:15px}
.news strong{display:block;font-size:11px;color:#666;text-decoration:underline;letter-spacing:.3px}
.news span{font-size:11px;color:#666;letter-spacing:.2px}
.news-rule{left:741px;width:222px;border-top:1px dotted #ccc}

/* bottom columns */
.col-text{font-size:11px;line-height:15.6px;color:#666;width:285px}
.svc{left:417px;width:283px;display:flex;align-items:center;gap:8px;font-size:11px;color:#666;padding-bottom:10px;border-bottom:1px dotted #ddd}
.svc.last{border-bottom:0}
.contact{left:746px;display:flex;align-items:center;gap:10px;font-size:12px;color:var(--brand-dark)}

/* footer */
.footer{left:0;top:1113px;width:1053px;height:87px;background:var(--footer);border-top:4px solid #eee}
.footer-nav{left:89px;top:1140px;font-size:11px;color:var(--footer-text);white-space:nowrap}
.footer-legal{left:89px;top:1165px;font-size:11px;color:#aaa;display:flex;gap:12px}
.footer-legal a{color:#fff;text-decoration:none;border-left:1px solid #777;padding-left:12px}
.footer-logo{left:827px;top:1141px;color:#bdbdbd;font-family:"Open Sans",sans-serif;line-height:1}
.footer-logo .name{font-size:30px;letter-spacing:1px;display:block}
.footer-logo .sub{font-size:8px;letter-spacing:9.5px;display:block;margin-top:2px}
</style>
</head>
<body>

<!-- top utility bar -->
<div class="abs top-mail">
  <svg width="24" height="16" viewBox="0 0 24 16"><rect x="1" y="1" width="22" height="14" fill="none" stroke="#666" stroke-width="2"/><path d="M1 1 L12 9 L23 1" fill="none" stroke="#666" stroke-width="2"/></svg>
  <span>hello@verbrookpartners.com</span>
</div>
<div class="abs search">
  <span>Enter Your Keywords Here...</span>
  <i><svg width="18" height="18" viewBox="0 0 18 18"><circle cx="7" cy="7" r="5.5" fill="none" stroke="#888" stroke-width="2.4"/><path d="M11 11 L16.5 16.5" stroke="#888" stroke-width="3"/></svg></i>
</div>
<div class="abs social" role="img" aria-label="Social media links"><b></b><b></b><b></b></div>

<!-- header -->
<div class="abs header"></div>
<div class="abs nav-marker"></div>
<div class="abs logo"><span class="name">VERBROOK</span><span class="sub">PARTNERS</span></div>
<nav class="abs nav">
  <a href="#">HOME</a>
  <a href="#">VERBROOK SERVICE LINES</a>
  <a href="#">THE VERBROOK STORY</a>
  <a href="#">VERBROOK CASE STUDIES</a>
  <a href="#">OUR PEOPLE</a>
  <a href="#">CONTACT VERBROOK</a>
</nav>

<!-- slider -->
<div class="abs slider" role="img" aria-label="Photo of a team of business consultants in suits standing with arms crossed in front of a grey world map"></div>
<div class="abs arrow" style="left:0"><svg width="24" height="36" viewBox="0 0 24 36"><path d="M20 2 L4 18 L20 34" fill="none" stroke="#666" stroke-width="5"/></svg></div>
<div class="abs arrow" style="left:985px"><svg width="24" height="36" viewBox="0 0 24 36"><path d="M4 2 L20 18 L4 34" fill="none" stroke="#666" stroke-width="5"/></svg></div>

<!-- welcome -->
<section class="abs welcome">
  <h1>WELCOME</h1>
  <div class="sep"></div>
  <p>There are many variations of passages of Lorem Ipsum available, but the majority have suffered alteration in some form, by injected humour, or randomised words which don't look even slightly believable.</p>
  <div class="btn">Learn More</div>
</section>

<div class="abs hr" style="top:608px"></div>

<!-- about us -->
<h2 class="abs" style="left:88px;top:637px">ABOUT US</h2>
<div class="abs card" style="left:88px">
  <div class="thumb" role="img" aria-label="Photo of two women studying at a desk"><div class="label">COACHING</div></div>
  <p>Lorem ipsum dolor sit amet, consectetuer adipiscing elit, sed diam nonummy nibh euismod</p>
</div>
<div class="abs card" style="left:297px">
  <div class="thumb" role="img" aria-label="Photo of colleagues talking in a bright office"><div class="label">COUNSELLING</div></div>
  <p>Lorem ipsum dolor sit amet, consectetuer adipiscing elit, sed diam nonummy nibh euismod</p>
</div>
<div class="abs card" style="left:507px">
  <div class="thumb" role="img" aria-label="Photo of a business meeting around a table"><div class="label">GUIDANCE</div></div>
  <p>Lorem ipsum dolor sit amet, consectetuer adipiscing elit, sed diam nonummy nibh euismod</p>
</div>
<a class="abs more" style="left:88px;top:887px">Learn More</a>
<a class="abs more" style="left:298px;top:887px">Learn More</a>
<a class="abs more" style="left:507px;top:887px">Learn More</a>

<div class="abs vr" style="left:723px;top:641px;height:223px"></div>

<!-- news -->
<h2 class="abs" style="left:744px;top:637px">NEWS &amp; UPDATES</h2>
<div class="abs news" style="top:690px">
  <svg width="36" height="35" viewBox="0 0 36 35"><rect x="2" y="4" width="32" height="29" rx="3" fill="#5a5a5a"/><rect x="6" y="13" width="24" height="17" fill="#fff"/><rect x="9" y="0" width="4" height="8" fill="#5a5a5a"/><rect x="23" y="0" width="4" height="8" fill="#5a5a5a"/><text x="18" y="27" font-family="Arimo,sans-serif" font-size="12" font-weight="700" fill="#5a5a5a" text-anchor="middle">12</text></svg>
  <div><strong>Lorem ipsum dolor sit amet,</strong><span>consectetuer adipiscing elit, sed</span></div>
</div>
<div class="abs news-rule" style="top:742px"></div>
<div class="abs news" style="top:759px">
  <svg width="36" height="35" viewBox="0 0 36 35"><rect x="2" y="4" width="32" height="29" rx="3" fill="#5a5a5a"/><rect x="6" y="13" width="24" height="17" fill="#fff"/><rect x="9" y="0" width="4" height="8" fill="#5a5a5a"/><rect x="23" y="0" width="4" height="8" fill="#5a5a5a"/><text x="18" y="27" font-family="Arimo,sans-serif" font-size="12" font-weight="700" fill="#5a5a5a" text-anchor="middle">12</text></svg>
  <div><strong>Lorem ipsum dolor sit amet,</strong><span>consectetuer adipiscing elit, sed</span></div>
</div>
<div class="abs news-rule" style="top:811px"></div>
<div class="abs news" style="top:827px">
  <svg width="36" height="35" viewBox="0 0 36 35"><rect x="2" y="4" width="32" height="29" rx="3" fill="#5a5a5a"/><rect x="6" y="13" width="24" height="17" fill="#fff"/><rect x="9" y="0" width="4" height="8" fill="#5a5a5a"/><rect x="23" y="0" width="4" height="8" fill="#5a5a5a"/><text x="18" y="27" font-family="Arimo,sans-serif" font-size="12" font-weight="700" fill="#5a5a5a" text-anchor="middle">12</text></svg>
  <div><strong>Lorem ipsum dolor sit amet,</strong><span>consectetuer adipiscing elit, sed</span></div>
</div>
<a class="abs more" style="left:745px;top:887px">Learn More</a>

<div class="abs hr" style="top:924px"></div>

<!-- research -->
<h2 class="abs blue" style="left:89px;top:951px">RESEARCH</h2>
<p class="abs col-text" style="left:89px;top:988px">Lorem ipsum dolor sit amet, consectetuer adipiscing elit, sed diam nonummy nibh euismod tincidunt ut laoreet dolore magna aliquam erat volutpat. Ut wisi enim ad minim veniam, quis nostrud exerci tation ullamcorper suscipit lobortis nisl ut aliquip ex ea commodo consequat.</p>
<div class="abs vr" style="left:389px;top:952px;height:132px"></div>

<!-- services -->
<h2 class="abs blue" style="left:417px;top:951px">SERVICES</h2>
<div class="abs svc" style="top:990px"><svg width="13" height="13" viewBox="0 0 13 13"><circle cx="6.5" cy="6.5" r="6.5" fill="#444"/><path d="M6.5 3.5v6M3.5 6.5h6" stroke="#fff" stroke-width="1.6"/></svg>Lorem Ipsum is simply dummy text of the and type...</div>
<div class="abs svc" style="top:1020px"><svg width="13" height="13" viewBox="0 0 13 13"><circle cx="6.5" cy="6.5" r="6.5" fill="#444"/><path d="M6.5 3.5v6M3.5 6.5h6" stroke="#fff" stroke-width="1.6"/></svg>Lorem Ipsum is simply dummy text of the and type...</div>
<div class="abs svc last" style="top:1051px"><svg width="13" height="13" viewBox="0 0 13 13"><circle cx="6.5" cy="6.5" r="6.5" fill="#444"/><path d="M6.5 3.5v6M3.5 6.5h6" stroke="#fff" stroke-width="1.6"/></svg>Lorem Ipsum is simply dummy text of the and type...</div>
<div class="abs vr" style="left:724px;top:952px;height:132px"></div>

<!-- contact -->
<h2 class="abs blue" style="left:744px;top:951px">CONTACT US</h2>
<div class="abs contact" style="top:990px"><svg width="15" height="13" viewBox="0 0 15 13"><path d="M7.5 0 L15 6.5 H13 V13 H9 V9 H6 V13 H2 V6.5 H0 Z" fill="var(--brand)"/></svg>Address Marlowe Lane 14c 4820 NY 10457</div>
<div class="abs contact" style="top:1019px"><svg width="15" height="12" viewBox="0 0 15 12"><path d="M0 4 Q7.5 -2 15 4 L12 5.5 L10.5 3.5 H4.5 L3 5.5 Z" fill="var(--brand)"/><rect x="3" y="6" width="9" height="6" rx="1" fill="var(--brand)"/></svg>+ 914-5502-377</div>
<div class="abs contact" style="top:1052px"><svg width="15" height="11" viewBox="0 0 15 11"><rect x="0" y="0" width="15" height="11" fill="var(--brand)"/><path d="M0 0 L7.5 6 L15 0" fill="none" stroke="#fff" stroke-width="1.4"/></svg>hello@verbrookpartners.com</div>

<!-- footer -->
<footer class="abs footer"></footer>
<div class="abs footer-nav">HOME - VERBROOK SERVICE LINES - THE VERBROOK STORY - VERBROOK CASE STUDIES - OUR PEOPLE - CONTACT VERBROOK</div>
<div class="abs footer-legal"><span>© 2013 verbrookpartners.com . All Rights Reserved</span><a href="#">Terms &amp; Conditions</a><a href="#">Privacy Policy</a></div>
<div class="abs footer-logo"><span class="name">VERBROOK</span><span class="sub">PARTNERS</span></div>

</body>
</html>
```